Business Card Colourful and fun Design Project

I need a business card design for my Ecommerce website which am launching soon. we are based in the United Arab Emirates and our customers are based in Dubai and other cities in UAE, In addition to our neighbour countries in the GCC. We sell Gadgets, fashion and other trendy stuff that are hard to find in our market. The company name is "ZIMTOWALRUS" logo consists of a panda wearing traditional local Arab thobe. would like to see a clean, colourful fun design to represent us.
Updates
please read the discussion board. thanks
Industry/Entity Type
Fashion
Look and feel
Each slider illustrates characteristics of the customer's brand and the style your logo design should communicate.

```html
<!DOCTYPE html>
<html lang="en">
<head>
<meta charset="utf-8">
<title>Zimtowalrus Business Card</title>
<link href="https://fonts.googleapis.com/css2?family=Arimo:wght@400;700&display=swap" rel="stylesheet">
<style>
  :root {
    --backdrop: #e9e9ea;
    --card: #f4f4f4;
    --card-edge: #dcdcdc;
    --red: #c8202a;
    --red-dark: #8f1219;
    --red-light: #e0545a;
    --text-grey: #6d6d6d;
    --role-grey: #9a9a9a;
    --mascot-tone: #d9d6d3;
    --mascot-edge: #b9b4b0;
  }
  * { margin: 0; padding: 0; box-sizing: border-box; }
  html, body {
    width: 1200px; height: 800px; overflow: hidden;
    background: var(--backdrop);
    font-family: "Arimo", Arial, sans-serif;
  }
  .sheet {
    position: relative; width: 1200px; height: 800px;
    display: flex; flex-direction: column; align-items: center; justify-content: center; gap: 36px;
  }
  .card {
    position: relative; width: 620px; height: 354px;
    background: var(--card);
    border: 1px solid var(--card-edge);
    box-shadow: 0 8px 22px rgba(0,0,0,0.14);
    overflow: hidden;
  }
  .card-bands { position: absolute; inset: 0; width: 100%; height: 100%; z-index: 0; }
  .card > :not(.card-bands) { z-index: 1; }
  .mascot {
    position: absolute;
    background: linear-gradient(160deg, var(--mascot-tone), var(--mascot-edge));
    border-radius: 10px;
  }
  .card-back .mascot { width: 120px; height: 140px; left: 250px; top: 107px; }
  .card-front .mascot { width: 56px; height: 74px; left: 34px; top: 34px; }
  .brand-name {
    position: absolute; left: 104px; top: 56px;
    font-weight: 700; font-size: 28px; letter-spacing: 1px;
    color: var(--red);
  }
  .contact-list {
    position: absolute; left: 410px; top: 132px;
    list-style: none; font-size: 14px; color: var(--text-grey); line-height: 1.25;
  }
  .contact-list li { display: flex; align-items: flex-start; gap: 12px; margin-bottom: 12px; }
  .contact-list svg { flex: none; width: 18px; height: 18px; fill: var(--red); }
  .person { position: absolute; left: 34px; bottom: 30px; }
  .person-name { font-weight: 700; font-size: 30px; color: var(--red); letter-spacing: -0.5px; }
  .person-role { font-size: 16px; color: var(--role-grey); margin-top: 2px; }
</style>
</head>
<body>
<main class="sheet">

  <section class="card card-back" aria-label="Card back">
    <svg class="card-bands" viewBox="0 0 620 354" aria-hidden="true">
      <g fill="none" stroke-linecap="round">
        <path d="M-20 90 C180 150 420 170 640 40" stroke="var(--red)" stroke-width="18"/>
        <path d="M-20 110 C180 170 420 190 640 62" stroke="var(--red-dark)" stroke-width="4"/>
        <path d="M-20 120 C180 180 420 200 640 74" stroke="var(--red-light)" stroke-width="2"/>
        <path d="M-20 300 C160 220 420 150 640 200" stroke="var(--red)" stroke-width="14"/>
        <path d="M-20 282 C160 202 420 132 640 182" stroke="var(--red-dark)" stroke-width="3"/>
        <path d="M60 380 C200 230 400 120 520 -20" stroke="var(--red)" stroke-width="16"/>
        <path d="M90 380 C230 230 420 130 560 -20" stroke="var(--red-dark)" stroke-width="5"/>
        <path d="M40 380 C190 240 380 120 490 -20" stroke="var(--red-light)" stroke-width="2"/>
      </g>
    </svg>
    <div class="mascot" role="img" aria-label="Mascot illustration: panda in a traditional white thobe and patterned headdress"></div>
  </section>

  <section class="card card-front" aria-label="Card front">
    <svg class="card-bands" viewBox="0 0 620 354" aria-hidden="true">
      <g fill="none" stroke-linecap="round">
        <path d="M-20 211 C150 211 300 96 640 -34" stroke="var(--red-light)" stroke-width="2"/>
        <path d="M-20 218 C150 218 300 103 640 -27" stroke="var(--red-dark)" stroke-width="3"/>
        <path d="M-20 228 C150 228 300 113 640 -17" stroke="var(--red)" stroke-width="14"/>
        <path d="M-20 240 C150 240 300 125 640 -5" stroke="var(--red-dark)" stroke-width="2"/>
        <path d="M-20 249 C150 249 300 134 640 4" stroke="var(--red)" stroke-width="8"/>
      </g>
    </svg>
    <div class="mascot" role="img" aria-label="Mascot illustration: panda in a traditional white thobe"></div>
    <div class="brand-name">ZIMTOWALRUS</div>
    <ul class="contact-list">
      <li>
        <svg viewBox="0 0 18 18" aria-hidden="true"><path d="M5 1h8a1 1 0 0 1 1 1v14a1 1 0 0 1-1 1H5a1 1 0 0 1-1-1V2a1 1 0 0 1 1-1zm1 2v10h6V3zm3 11.2a.9.9 0 1 0 0 1.8.9.9 0 0 0 0-1.8z"/></svg>
        <span>800 WALRUS (925787)</span>
      </li>
      <li>
        <svg viewBox="0 0 18 18" aria-hidden="true"><path d="M1 2h16v11H1zm2 2v7h12V4zM7 14h4v1.5h2V17H5v-1.5h2z"/></svg>
        <span>http://www.Zimtowalrus.com</span>
      </li>
      <li>
        <svg viewBox="0 0 18 18" aria-hidden="true"><path d="M9 1a6 6 0 0 1 6 6c0 4.5-6 10-6 10S3 11.5 3 7a6 6 0 0 1 6-6zm0 3.5a2.5 2.5 0 1 0 0 5 2.5 2.5 0 0 0 0-5z"/></svg>
        <span>48 Harlow st.<br>Cedar Brook Valley<br>Westport city<br>2140</span>
      </li>
    </ul>
    <div class="person">
      <div class="person-name">Marek Holloway</div>
      <div class="person-role">Sales Executive</div>
    </div>
  </section>

</main>
</body>
</html>
```